Riverpeak Analytics needs new design business card

We are video surveillance and analytics software development company.
I am looking for a professional business card.
Our website is www.riverpeakanalytics.example.au
Please have a loo and get the feel for who we are and what we do.
I do not know what else to give you apart from good luck and I hope your design gets selected.
Thank you very much for participating
Business
Contact Information for Business Card
Address
27/15 Marlowe Street Fernbrook NSW 2199
Telephone 1300 582 417
Mobile 0450 731 258
email: marcus@riverpeakanalytics.example.au
name
Marcus Helvard
Position
Managing Director
Font styles to use
Other font styles liked:
- Arial
Look and feel

```html
<!DOCTYPE html>
<html lang="en">
<head>
<meta charset="utf-8">
<title>Riverpeak Analytics – Business Card</title>
<link href="https://fonts.googleapis.com/css2?family=Open+Sans:wght@400;600;700;800&display=swap" rel="stylesheet">
<style>
  :root {
    --backdrop: #e9e6e1;
    --card: #ffffff;
    --navy: #1c3764;
    --blue: #1f5fa6;
    --band: #2a6db5;
    --orange: #f0a030;
    --tab-grey: #8a9aa8;
    --text: #234a82;
  }
  * { margin: 0; padding: 0; box-sizing: border-box; }
  html, body {
    width: 1200px; height: 900px; overflow: hidden;
    background: var(--backdrop);
    font-family: "Open Sans", Arial, sans-serif;
  }
  .card {
    position: absolute; left: 280px;
    width: 640px; height: 360px;
    background: var(--card);
    border-radius: 18px;
    box-shadow: 0 6px 18px rgba(0,0,0,.15);
    overflow: hidden;
  }
  .card--front { top: 60px; display: flex; align-items: center; justify-content: center; }
  .card--back { top: 480px; }

  .brand {
    display: flex; align-items: center; gap: 16px;
    color: var(--navy); font-weight: 800; text-transform: uppercase;
    letter-spacing: 1px;
  }
  .brand__mark { width: 34px; height: 34px; border-radius: 50%; background: var(--navy); }
  .card--front .brand__name { font-size: 44px; }

  .card--back .brand { position: absolute; left: 40px; top: 96px; }
  .card--back .brand__mark { width: 28px; height: 28px; }
  .card--back .brand__name { font-size: 30px; }

  .person { position: absolute; right: 46px; top: 26px; text-align: right; }
  .person__name { color: var(--blue); font-weight: 700; font-size: 24px; }
  .person__role { color: var(--orange); font-weight: 400; font-size: 15px; }

  .tab { position: absolute; background: var(--tab-grey); border-radius: 3px; }
  .tab--right { right: 0; top: 26px; width: 12px; height: 30px; }
  .tab--left { left: 0; top: 210px; width: 12px; height: 62px; }

  .contact { position: absolute; left: 40px; top: 196px; list-style: none; }
  .contact li {
    display: flex; align-items: center; gap: 12px;
    color: var(--text); font-size: 17px; line-height: 24px;
  }
  .contact svg { width: 16px; height: 16px; flex: none; }

  .footer-rule {
    position: absolute; left: 0; right: 0; bottom: 62px;
    height: 2px; background: var(--orange);
  }
  .address-band {
    position: absolute; left: 0; right: 0; bottom: 0; height: 56px;
    background: var(--band);
    border-radius: 40px 0 0 0;
    display: flex; align-items: center; justify-content: center;
    color: #fff; font-weight: 700; font-size: 18px; letter-spacing: .3px;
  }
</style>
</head>
<body>
  <section class="card card--front">
    <div class="brand"><span class="brand__mark"></span><span class="brand__name">Riverpeak Analytics</span></div>
  </section>

  <section class="card card--back">
    <span class="tab tab--right"></span>
    <span class="tab tab--left"></span>

    <div class="person">
      <p class="person__name">Marcus Helvard</p>
      <p class="person__role">Managing Director</p>
    </div>

    <div class="brand"><span class="brand__mark"></span><span class="brand__name">Riverpeak Analytics</span></div>

    <ul class="contact">
      <li>
        <svg viewBox="0 0 16 16" aria-hidden="true"><path d="M4 1l3 3-2 2c1 2 3 4 5 5l2-2 3 3-2 2C7 14 2 9 2 3z" fill="none" stroke="#f0a030" stroke-width="1.4"/></svg>
        1300 582 417
      </li>
      <li>
        <svg viewBox="0 0 16 16" aria-hidden="true"><rect x="4" y="1" width="8" height="14" rx="1.5" fill="none" stroke="#f0a030" stroke-width="1.4"/><circle cx="8" cy="12.5" r=".9" fill="#f0a030"/></svg>
        0450 731 258
      </li>
      <li>
        <svg viewBox="0 0 16 16" aria-hidden="true"><circle cx="8" cy="8" r="6.5" fill="none" stroke="#f0a030" stroke-width="1.4"/><path d="M1.5 8h13M8 1.5c-3 3.5-3 9.5 0 13M8 1.5c3 3.5 3 9.5 0 13" fill="none" stroke="#f0a030" stroke-width="1.1"/></svg>
        www.riverpeakanalytics.example.au
      </li>
      <li>
        <svg viewBox="0 0 16 16" aria-hidden="true"><rect x="1.5" y="3.5" width="13" height="9" fill="none" stroke="#f0a030" stroke-width="1.4"/><path d="M1.5 3.5L8 9l6.5-5.5" fill="none" stroke="#f0a030" stroke-width="1.4"/></svg>
        marcus@riverpeakanalytics.example.au
      </li>
    </ul>

    <span class="footer-rule"></span>
    <div class="address-band">27/15 Marlowe Street Fernbrook NSW 2199</div>
  </section>
</body>
</html>
```